Funeral Services Web Site

We need a website for a Funeral Services company. The choice of colors is free of charge. One Page Website with 8 sections. Menu: - Home - Our Services - Obituaries -> link to another page. - Our Shop - Funeral Monument - Funeral Contract - Contact Us

Target Market(s)

Every one need Funeral Services

Coding

Coded - Design and coding required

Number of Pages Required

2 page

Font styles to use
Sans Serif
Script

Colors

Designer to choose colors to be used in the design.

```html
<!DOCTYPE html>
<html lang="en">
<head>
<meta charset="utf-8">
<title>Maison Verlaine – Funeral Services</title>
<link href="https://fonts.googleapis.com/css2?family=Poppins:wght@400;500;600;700&family=Roboto:wght@700&family=Lobster&display=swap" rel="stylesheet">
<style>
:root{
  --gold:#a0782e;
  --brown:#6b5335;
  --brown-dark:#5e4c39;
  --card:#6d5c4a;
  --card-dark:#5a4a38;
  --text:#333;
  --muted:#555;
  --shop-bg:#e9e7e4;
  --white:#fff;
}
*{margin:0;padding:0;box-sizing:border-box}
html,body{width:1200px;height:4222px;overflow:hidden}
body{position:relative;font-family:'Poppins',sans-serif;color:var(--text);background:var(--white)}
.abs{position:absolute}
.heading{font-family:'Roboto',sans-serif;font-weight:700;font-size:40px;color:var(--brown);letter-spacing:.3px}
.btn{position:absolute;display:flex;align-items:center;justify-content:center;background:var(--gold);color:var(--white);font-weight:600;font-size:15px;border-radius:3px}

/* header */
.header{top:0;left:0;width:1200px;height:212px}
.call-icon{left:144px;top:50px;width:58px;height:58px;border-radius:50%;background:#5a5048}
.call-label{left:222px;top:50px;font-size:19px;color:#4a4a4a}
.call-number{left:222px;top:78px;font-size:25px;font-weight:600;color:var(--brown)}
.brand{left:850px;top:46px;display:flex;align-items:center;gap:12px;font-size:27px;font-weight:600;color:var(--brown)}
.brand-dot{width:38px;height:38px;border-radius:50%;background:var(--brown)}
.nav{left:0;top:170px;width:1200px;display:flex;justify-content:center;gap:31px;font-size:13.5px;color:var(--text)}

/* hero */
.hero{top:212px;left:0;width:1200px;height:690px;background:linear-gradient(100deg,#3b1c14 0%,#6b2a1e 35%,#5a4634 60%,#8a8171 85%,#6f6555 100%)}
.hero-title{top:235px;width:1200px;text-align:center;font-family:'Lobster',cursive;font-size:80px;color:var(--white)}
.hero-text{top:350px;left:180px;width:840px;text-align:center;font-size:21px;line-height:37px;color:var(--white)}
.hero-btn{left:510px;top:440px;width:180px;height:48px;font-size:17px}
.arrow{width:38px;height:38px;border-radius:50%}
.hero .arrow{background:rgba(255,255,255,.12)}
.hero-edge{left:0;bottom:0}

/* funeral home */
.home-title{left:144px;top:1048px}
.home-text{left:144px;top:1110px;width:394px;font-size:13.8px;line-height:28.7px;color:var(--text)}
.home-text p+p{margin-top:20px}
.home-btn{left:144px;top:1387px;width:142px;height:50px}
.home-frame{left:640px;top:1015px}
.home-photo{left:595px;top:1030px;width:525px;height:422px;border:2px solid var(--gold);background:linear-gradient(180deg,#6f6c66 0%,#c8c3b8 40%,#9c9487 75%,#5a544c 100%)}

/* services */
.services{top:1572px;left:0;width:1200px;height:785px;background:var(--brown-dark)}
.services-title{top:78px;width:1200px;text-align:center;color:var(--white)}
.svc-card{width:444px;height:249px;background:var(--card);overflow:hidden}
.svc-corner{left:0;top:0}
.svc-body{left:142px;top:30px;width:280px;color:var(--white)}
.svc-body h3{font-size:16.5px;font-weight:600;line-height:27px;margin-bottom:5px}
.svc-body p{font-size:13px;line-height:26px;color:#eee}
.svc-btn{position:absolute;left:142px;top:184px;width:104px;height:30px;border:2px solid var(--gold);border-radius:3px;font-size:11.5px;font-weight:600;display:flex;align-items:center;justify-content:center;color:var(--white)}
.services .arrow{border:1.5px solid var(--white)}

/* obituaries */
.obit-title{top:2485px;width:1200px;text-align:center}
.obit-intro{top:2543px;left:330px;width:540px;text-align:center;font-size:14px;line-height:26px;color:var(--text)}
.person{width:194px;text-align:center}
.portrait{width:130px;height:130px;border-radius:50%;margin:0 auto 12px;background:radial-gradient(circle at 50% 40%,#c9b3a0 0%,#8d7b6c 60%,#5b5048 100%);border:2px solid #ddd}
.person .name{font-size:13px;color:var(--brown)}
.person .dates{font-size:9.5px;font-weight:600;color:#444;margin-top:2px}
.obit-btn{left:524px;top:3100px;width:152px;height:44px;font-size:14px}

/* shop */
.shop{top:3228px;left:0;width:1200px;height:554px;background:var(--shop-bg)}
.shop-photo{left:0;top:0;width:605px;height:554px;background:linear-gradient(135deg,#7a5a30 0%,#b48a4e 40%,#c9a774 60%,#dcd7cf 100%)}
.shop-title{left:631px;top:115px}
.shop-text{left:631px;top:176px;width:440px;font-size:13.8px;line-height:27px}
.shop-list{left:631px;top:268px;list-style:none;font-size:14px;line-height:37px}
.shop-list li{display:flex;align-items:center;gap:10px}
.shop-btn{left:631px;top:412px;width:118px;height:38px;font-weight:400;font-size:14px}

/* footer */
.f-brand{left:144px;top:3900px;display:flex;align-items:center;gap:12px;font-size:26px;font-weight:600;color:var(--brown)}
.f-title{font-size:17px;font-weight:600;color:var(--brown)}
.f-contact{left:440px;top:3870px}
.f-contact ul{list-style:none;margin-top:12px;font-size:13.5px;line-height:34px}
.f-contact li{display:flex;align-items:center;gap:12px}
.socials{display:flex;gap:8px;margin-top:16px}
.socials span{width:47px;height:47px;border-radius:50%;border:1.5px solid var(--brown);display:block}
.f-touch{left:785px;top:3870px}
.field{position:absolute;border:1px solid #bbb;font-size:11px;color:#777;padding:6px 10px}
.send{position:absolute;left:0;top:192px;width:104px;height:36px;border:2px solid var(--brown);border-radius:3px;font-size:12px;font-weight:600;color:var(--brown);display:flex;align-items:center;justify-content:center}
.f-line{left:144px;top:4147px;width:912px;height:1px;background:#ccc}
.copyright{top:4172px;width:1200px;text-align:center;font-size:13px;color:var(--text)}
</style>
</head>
<body>

<header class="header abs">
  <div class="call-icon abs">
    <svg width="58" height="58" viewBox="0 0 58 58"><path d="M21 18c2-1 4 3 5 5s-2 3-1 5c1 3 4 6 7 7 2 1 3-2 5-1s6 3 5 5-4 4-6 4c-8-1-18-11-19-19 0-2 2-5 4-6z" fill="none" stroke="#fff" stroke-width="1.8"/></svg>
  </div>
  <div class="call-label abs">CALL US AT</div>
  <div class="call-number abs">064 / 22.41.90</div>
  <div class="brand abs"><span class="brand-dot"></span>Maison Verlaine</div>
  <nav class="nav abs">
    <span>HOME</span><span>OUR SERVICES</span><span>OBITUARIES</span><span>OUR SHOP</span><span>FUNERAL MONUMENT</span><span>FUNERAL CONTRACT</span><span>CONTACT US</span>
  </nav>
</header>

<section class="hero abs" role="img" aria-label="Photograph of a polished wooden coffin with a white flower arrangement">
  <h1 class="hero-title abs">Maison Verlaine</h1>
  <p class="hero-text abs">Sed ut perspiciatis unde omnis iste natus saror sit voluptatem accusantium doloremque laudantium, totam rem aperiam, eaque ipsa quae ab illo</p>
  <div class="btn hero-btn">GET STARTED</div>
  <div class="arrow abs" style="left:41px;top:351px"><svg width="38" height="38"><path d="M22 12l-7 7 7 7" fill="none" stroke="#fff" stroke-width="2.5"/></svg></div>
  <div class="arrow abs" style="left:1118px;top:351px"><svg width="38" height="38"><path d="M16 12l7 7-7 7" fill="none" stroke="#fff" stroke-width="2.5"/></svg></div>
  <svg class="hero-edge abs" width="1200" height="90" viewBox="0 0 1200 90"><path d="M0 30 L40 38 60 22 90 40 120 28 150 45 200 36 240 50 300 42 360 58 420 50 480 62 540 48 600 70 660 55 720 60 780 44 840 52 900 40 960 46 1010 30 1060 38 1110 26 1160 34 1200 28 L1200 90 L0 90Z" fill="#fff"/></svg>
</section>

<h2 class="heading home-title abs">OUR FUNERAL HOME</h2>
<div class="home-text abs">
  <p>Located in the heart of Valmont, our funeral home is equipped with several private lounges that guarantee privacy and calm, as well as a cafeteria space. In addition, we benefit from a complete infrastructure for the preparation and reception of the deceased: a treatment room adapted to thanatopraxy, a cold room, ...</p>
  <p>Our funeral home has a large private parking opposite its main entrance, rue du Parc.</p>
</div>
<div class="btn home-btn">READ MORE</div>
<svg class="home-frame abs" width="500" height="452" viewBox="0 0 500 452"><path d="M0 0 H500 V452 H0 V437 H480 V15 H10z" fill="#5e4c39"/></svg>
<div class="home-photo abs" role="img" aria-label="Photograph of a viewing room with curtains, a crucifix and candle stands"></div>

<section class="services abs">
  <h2 class="heading services-title abs">OUR SERVICES</h2>
  <div class="arrow abs" style="left:50px;top:379px"><svg width="38" height="38"><path d="M21 13l-6 6 6 6" fill="none" stroke="#fff" stroke-width="1.5"/></svg></div>
  <div class="arrow abs" style="left:1118px;top:379px"><svg width="38" height="38"><path d="M17 13l6 6-6 6" fill="none" stroke="#fff" stroke-width="1.5"/></svg></div>

  <article class="svc-card abs" style="left:144px;top:166px">
    <svg class="svc-corner abs" width="120" height="120"><path d="M0 0H120A120 120 0 0 1 0 120Z" fill="#5a4a38"/><path d="M12 50l18-14 14 8 16-8 18 14-22 20-12-8z" fill="none" stroke="#fff" stroke-width="2"/></svg>
    <div class="svc-body abs"><h3>Personalized &amp; dignified support from the first moments</h3><p>Funeral Maison Verlaine assist you and advise you when a loved one dies.</p></div>
    <span class="svc-btn">LEARN MORE</span>
  </article>
  <article class="svc-card abs" style="left:610px;top:166px">
    <svg class="svc-corner abs" width="120" height="120"><path d="M0 0H120A120 120 0 0 1 0 120Z" fill="#5a4a38"/><path d="M24 34h34l12 12v44H24z M58 34v12h12 M34 58h26 M34 66h26 M34 74h26 M34 82h20" fill="none" stroke="#fff" stroke-width="2"/></svg>
    <div class="svc-body abs"><h3>Assistance in all administrative procedures</h3><p>Because the loss of a loved one causes a lot of steps, we help you accomplish them.</p></div>
    <span class="svc-btn">LEARN MORE</span>
  </article>
  <article class="svc-card abs" style="left:144px;top:445px">
    <svg class="svc-corner abs" width="120" height="120"><path d="M0 0H120A120 120 0 0 1 0 120Z" fill="#5a4a38"/><rect x="22" y="46" width="56" height="24" rx="3" fill="none" stroke="#fff" stroke-width="2"/><path d="M32 46v14 M42 46v14 M52 46v14 M62 46v14" stroke="#fff" stroke-width="2"/></svg>
    <div class="svc-body abs"><h3>Offer him his song to pay him a last tribute</h3><p>Because a personalized song is an ideal way to pay tribute to a deceased by professional musicians</p></div>
    <span class="svc-btn">LEARN MORE</span>
  </article>
  <article class="svc-card abs" style="left:610px;top:445px">
    <svg class="svc-corner abs" width="120" height="120"><path d="M0 0H120A120 120 0 0 1 0 120Z" fill="#5a4a38"/><circle cx="48" cy="46" r="16" fill="none" stroke="#fff" stroke-width="2"/><path d="M42 62l-6 26 M54 62l6 26 M48 62v26" stroke="#fff" stroke-width="2"/></svg>
    <div class="svc-body abs"><h3>Put down your last wishes to guarantee their respect!</h3><p>Filing of last wishes with the municipal administration compels the funeral director to comply with it.</p></div>
    <span class="svc-btn">LEARN MORE</span>
  </article>
</section>

<h2 class="heading obit-title abs">OBITUARIES</h2>
<p class="obit-intro abs">Ut enim ad minima veniam, quis nostrum exercitationem ullam suscipit laboriosam, nisiut aliquid commodi conseuat.</p>

<div class="person abs" style="left:116px;top:2635px"><div class="portrait" role="img" aria-label="Portrait photograph"></div><div class="name">Mr Paolo FERRINI</div><div class="dates">07-29-1960 to 04-23-2019</div></div>
<div class="person abs" style="left:311px;top:2635px"><div class="portrait" role="img" aria-label="Portrait photograph"></div><div class="name">Mr Daniel VERMOT</div><div class="dates">03-23-1952 to 04-12-2019</div></div>
<div class="person abs" style="left:505px;top:2635px"><div class="portrait" role="img" aria-label="Portrait photograph"></div><div class="name">Mrs Odette LAMY</div><div class="dates">03-01-1929 to 04-09-2019</div></div>
<div class="person abs" style="left:700px;top:2635px"><div class="portrait" role="img" aria-label="Portrait photograph"></div><div class="name">Mrs. Irène COLSON</div><div class="dates">10-27-1940 to 02-04-2019</div></div>
<div class="person abs" style="left:894px;top:2635px"><div class="portrait" role="img" aria-label="Portrait photograph"></div><div class="name">Mrs Simone DELVAUX</div><div class="dates">08-02-1929 to 03-10-2019</div></div>

<div class="person abs" style="left:116px;top:2863px"><div class="portrait" role="img" aria-label="Portrait photograph"></div><div class="name">Mr Marcel PIRET</div><div class="dates">07-08-1954 to 03-06-2019</div></div>
<div class="person abs" style="left:311px;top:2863px"><div class="portrait" role="img" aria-label="Portrait photograph"></div><div class="name">Mrs Germaine NOLET</div><div class="dates">08-17-1930 to 02-23-2019</div></div>
<div class="person abs" style="left:505px;top:2863px"><div class="portrait" role="img" aria-label="Portrait photograph"></div><div class="name">Mr Julien MARCHAL</div><div class="dates">09-17-1985 to 04-01-2019</div></div>
<div class="person abs" style="left:700px;top:2863px"><div class="portrait" role="img" aria-label="Portrait photograph"></div><div class="name">Mr André THIRY</div><div class="dates">10-28-1935 to 03-29-2019</div></div>
<div class="person abs" style="left:894px;top:2863px"><div class="portrait" role="img" aria-label="Portrait photograph"></div><div class="name">Mrs Lucie DORVAL</div><div class="dates">06-27-1930 to 03-07-2019</div></div>

<div class="btn obit-btn">VIEW MORE</div>

<section class="shop abs">
  <div class="shop-photo abs" role="img" aria-label="Photograph of the shop with wooden coffins and silk flower wreaths"></div>
  <h2 class="heading shop-title abs">OUR SHOP</h2>
  <p class="shop-text abs">Adjacent to our funeral home and accessible by Tilleuls Street, our store offers a wide selection of silk flowers and funeral items.</p>
  <ul class="shop-list abs">
    <li><svg width="13" height="13"><circle cx="6.5" cy="6.5" r="6.5" fill="#6b5335"/><path d="M3.5 6.8l2 2 4-4" fill="none" stroke="#fff" stroke-width="1.6"/></svg>Ut enim ad minima veniam, quis nostrum exercitation</li>
    <li><svg width="13" height="13"><circle cx="6.5" cy="6.5" r="6.5" fill="#6b5335"/><path d="M3.5 6.8l2 2 4-4" fill="none" stroke="#fff" stroke-width="1.6"/></svg>Sed ut perspiciatis unde omnis iste natus voluptatem</li>
    <li><svg width="13" height="13"><circle cx="6.5" cy="6.5" r="6.5" fill="#6b5335"/><path d="M3.5 6.8l2 2 4-4" fill="none" stroke="#fff" stroke-width="1.6"/></svg>Doloremque laudantium, totam rem aperiam, eaqueqaous</li>
  </ul>
  <div class="btn shop-btn">READ MORE</div>
</section>

<footer>
  <div class="f-brand abs"><span class="brand-dot"></span>Maison Verlaine</div>
  <div class="f-contact abs">
    <div class="f-title">CONTACT US</div>
    <ul>
      <li><svg width="12" height="14"><path d="M6 13C2 8 1 6 1 5a5 5 0 0 1 10 0c0 1-1 3-5 8z" fill="#6b5335"/><circle cx="6" cy="5" r="1.8" fill="#fff"/></svg>12, Rue des Tilleuls 7100 - Valmont</li>
      <li><svg width="12" height="14"><path d="M2 1h3l1 3-2 1.5a7 7 0 0 0 4 4L9.5 8l3 1v3a1 1 0 0 1-1 1C6 13 1 8 1 2a1 1 0 0 1 1-1z" fill="#6b5335"/></svg>(064) / 224190</li>
      <li><svg width="12" height="14"><rect x="0" y="3" width="12" height="9" fill="#6b5335"/><path d="M0 3l6 5 6-5" fill="none" stroke="#fff" stroke-width="1"/></svg>contact@maison-verlaine.com</li>
    </ul>
    <div class="socials"><span></span><span></span><span></span></div>
  </div>
  <div class="f-touch abs">
    <div class="f-title">GET IN TOUCH</div>
    <div class="field" style="left:0;top:35px;width:129px;height:30px">First Name</div>
    <div class="field" style="left:140px;top:35px;width:130px;height:30px">Last Name</div>
    <div class="field" style="left:0;top:75px;width:129px;height:30px">Phone No</div>
    <div class="field" style="left:140px;top:75px;width:130px;height:30px">Email</div>
    <div class="field" style="left:0;top:118px;width:270px;height:62px">Message</div>
    <span class="send">SEND NOW</span>
  </div>
  <div class="f-line abs"></div>
  <p class="copyright abs">Copyrights © 2019 All rights reserved.</p>
</footer>

</body>
</html>
```